Kestrim LLC, needs a web page no more than 5 pages (for now)

Kestrim is a general contractor. Our services include general contracting, design-build construction, disaster recovery and environmental remediation. Our main clients are KZE, HJ, State and Local Gov't Agencies, Hospitals and Schools. Kestrim is also a SDVOSB.

```html
<!DOCTYPE html>
<html lang="en">
<head>
<meta charset="utf-8">
<title>Kestrim LLC — Where Integrity Meets Innovation in Construction</title>
<link href="https://fonts.googleapis.com/css2?family=Montserrat:wght@400;500;600;700&display=swap" rel="stylesheet">
<style>
:root{
  --bg:#1b1b1b;
  --bg-deep:#141414;
  --gold:#e39e2f;
  --gold-light:#f2bf5e;
  --gold-grad:linear-gradient(135deg,#d98f1f 0%,#f0b95a 100%);
  --text:#ffffff;
  --muted:#d6d6d6;
  --badge:#2c4478;
}
*{margin:0;padding:0;box-sizing:border-box}
html,body{width:1200px;height:4280px;overflow:hidden}
body{background:var(--bg);color:var(--text);font-family:"Montserrat",sans-serif;position:relative}
.abs{position:absolute}
a{color:inherit;text-decoration:none}
.btn{position:absolute;display:flex;align-items:center;justify-content:center;background:var(--gold-grad);color:#fff;border-radius:26px;font-size:15px;font-weight:500;letter-spacing:.3px;height:50px}
.gold{color:var(--gold)}
/* header */
.site-header{left:0;top:0;width:1200px;height:124px;background:var(--bg-deep);border-bottom:2px solid var(--gold)}
.nav{position:absolute;top:50px;font-size:15px;font-weight:500;letter-spacing:.2px;display:flex;gap:20px}
.nav .active{color:var(--gold)}
.brand{position:absolute;display:flex;align-items:center;gap:10px;font-weight:500;letter-spacing:1px}
.brand .mark{width:14px;height:14px;border-radius:50%;background:var(--gold)}
/* hero */
.hero{left:0;top:126px;width:1200px;height:657px;background:linear-gradient(180deg,#4a3a2c 0%,#6b5a48 28%,#3b3d44 60%,#22252b 100%)}
.hero-title{left:0;top:328px;width:1200px;text-align:center;font-size:49px;font-weight:700;line-height:63px;text-transform:uppercase}
/* photo blocks */
.photo{position:absolute;border-radius:16px}
/* section headings */
.sec-title{position:absolute;font-size:33px;font-weight:500;text-transform:uppercase;letter-spacing:.5px}
.copy{position:absolute;font-size:15px;line-height:30px;text-align:center;color:var(--muted)}
/* services */
.card{position:absolute;top:1645px;width:281px;height:255px;border:1.5px solid #9a9a9a;border-radius:10px;padding:0 21px}
.card.featured{background:var(--gold-grad);border-color:transparent}
.card svg{position:absolute;left:22px;top:28px;width:60px;height:60px;fill:none;stroke:var(--gold);stroke-width:2}
.card.featured svg{stroke:#fff}
.card h3{position:absolute;left:21px;top:118px;font-size:19px;font-weight:500;line-height:26px;width:240px}
.card p{position:absolute;left:21px;font-size:13px;line-height:22px;color:#e6e6e6;width:240px}
.card.featured p{color:#fbe3b8}
/* why */
.why-item{position:absolute;left:114px;width:460px}
.why-item h4{font-size:19px;font-weight:500;display:flex;align-items:center;gap:12px;margin-bottom:10px}
.why-item p{font-size:15px;line-height:23px;color:var(--muted)}
.tick{width:30px;height:30px}
/* clients */
.client{position:absolute;top:3005px;width:182px;height:160px;border:1.5px solid #a0a0a0;border-radius:8px;display:flex;align-items:center;justify-content:center;text-align:center;font-size:16px;font-weight:600;letter-spacing:.5px;text-transform:uppercase;padding:12px}
.client.featured{background:var(--gold-grad);border-color:transparent}
/* footer */
.foot-head{position:absolute;top:3935px;font-size:19px;font-weight:600;color:var(--gold);text-transform:uppercase}
.foot-links{position:absolute;left:530px;top:3982px;font-size:16px;line-height:39px;text-transform:uppercase}
.contact-row{position:absolute;left:792px;display:flex;align-items:center;gap:12px;font-size:15px}
.ico{width:30px;height:30px;border-radius:50%;background:var(--gold);display:flex;align-items:center;justify-content:center}
.ico svg{width:16px;height:16px;fill:#fff}
.badge{position:absolute;border-radius:50%;background:var(--badge);border:4px solid #e8e8e8}
.bottom-bar{left:0;top:4245px;width:1200px;height:35px;background:var(--gold-grad);text-align:center;font-size:13px;line-height:35px;color:#fff4dc}
</style>
</head>
<body>

<header class="abs site-header">
  <nav class="nav" style="left:125px">
    <a class="active">HOME</a><a>ABOUT US</a><a>SERVICES</a><a>PROJECTS</a>
  </nav>
  <div class="brand" style="left:520px;top:46px;font-size:29px"><span class="mark"></span>KESTRIM</div>
  <nav class="nav" style="left:721px;top:45px">
    <a>CLIENTS &amp; CERTIFICATIONS</a><a>CONTACT</a>
  </nav>
</header>

<section class="abs hero" role="img" aria-label="Aerial photograph of a city skyline at dusk"></section>
<h1 class="abs hero-title">Where Integrity Meets<br>Innovation in Construction</h1>
<a class="btn" style="left:474px;top:505px;width:252px">REQUEST A PROPOSAL</a>

<!-- who we are -->
<div class="photo" style="left:0;top:903px;width:288px;height:317px;border-radius:0 16px 16px 0;background:linear-gradient(135deg,#6d6a66,#c9b89a 60%,#d8a22a)" role="img" aria-label="Photo of a handshake over construction plans and a hard hat"></div>
<h2 class="sec-title" style="left:0;top:902px;width:1200px;text-align:center">Who <span class="gold">We Are</span></h2>
<p class="copy" style="left:330px;top:965px;width:540px">At <span class="gold">Kestrim,</span> we are more than a construction company — we are a Service-Disabled Veteran-Owned Small Business <span class="gold">(SDVOSB)</span> built on the principles of integrity, discipline, and mission success.</p>
<p class="copy" style="left:330px;top:1075px;width:540px">Our team brings decades of combined experience in general contracting, design-build construction, disaster recovery, and environmental remediation. We understand the importance of delivering projects on time, on budget, and to the highest standards.</p>
<a class="btn" style="left:496px;top:1230px;width:207px">MEET KESTRIM</a>
<div class="badge" style="left:920px;top:882px;width:110px;height:135px;border-radius:50% 50% 12px 12px" aria-label="Certification badge"></div>
<div class="badge" style="left:1055px;top:882px;width:140px;height:140px" aria-label="Certification badge"></div>
<div class="photo" style="left:917px;top:1045px;width:283px;height:317px;border-radius:16px 0 0 16px;background:linear-gradient(135deg,#3b4150,#7b7f87 50%,#c99a2c)" role="img" aria-label="Photo of an engineer in a hard hat and safety vest reviewing a clipboard"></div>

<!-- services -->
<h2 class="sec-title" style="left:0;top:1438px;width:1200px;text-align:center">Our <span class="gold">Services</span></h2>
<p class="copy" style="left:230px;top:1510px;width:740px">At Kestrim, we deliver <span class="gold" style="font-weight:600">mission-ready construction solutions</span> with the expertise and reliability trusted by government agencies, healthcare systems, and educational institutions. Our core services include:</p>

<div class="card featured" style="left:112px">
  <svg viewBox="0 0 60 60"><path d="M10 4h26l10 10v22M10 4v40h14"/><path d="M16 16h18M16 24h22M16 32h12"/><path d="M26 46l8-6 8 4 10-6M26 46l8 8 6-4 12 0"/></svg>
  <h3>General Contracting</h3>
  <p style="top:152px">Full-service project management from planning to completion, ensuring quality, efficiency, and</p>
</div>
<div class="card" style="left:460px">
  <svg viewBox="0 0 60 60"><circle cx="30" cy="30" r="10"/><circle cx="30" cy="30" r="18"/><path d="M30 6v6M30 48v6M6 30h6M48 30h6M13 13l4 4M43 43l4 4M13 47l4-4M43 17l4-4"/></svg>
  <h3>Disaster Recovery</h3>
  <p style="top:152px">Rapid deployment teams ready to restore facilities and infrastructure after natural disasters, ensuring</p>
</div>
<div class="card" style="left:809px">
  <svg viewBox="0 0 60 60"><path d="M8 8h28v44H8z"/><path d="M14 18h16M14 26h10"/><circle cx="38" cy="36" r="9"/><path d="M44 42l10 10"/></svg>
  <h3>Environmental<br>Remediation</h3>
  <p style="top:172px">Safe, compliant, and sustainable cleanup and restoration services</p>
</div>
<a class="btn" style="left:469px;top:1953px;width:262px">EXPLORE OUR SERVICES</a>

<!-- why choose -->
<h2 class="sec-title" style="left:114px;top:2163px;text-transform:none">WHY CHOOSE <span class="gold">KESTRIM</span></h2>

<div class="why-item" style="top:2247px"><h4><svg class="tick" viewBox="0 0 30 30"><circle cx="15" cy="15" r="12" fill="none" stroke="#e39e2f" stroke-width="2.5"/><path d="M9 15l5 5 12-14" fill="none" stroke="#e39e2f" stroke-width="3"/></svg>Veteran-Led &amp; Certified SDVOSB</h4><p>A trusted partner recognized for excellence and accountability.</p></div>
<div class="why-item" style="top:2355px"><h4><svg class="tick" viewBox="0 0 30 30"><circle cx="15" cy="15" r="12" fill="none" stroke="#e39e2f" stroke-width="2.5"/><path d="M9 15l5 5 12-14" fill="none" stroke="#e39e2f" stroke-width="3"/></svg>Proven Government Experience</h4><p>Successfully serving the KZE, HJ, state and local agencies, hospitals, and schools.</p></div>
<div class="why-item" style="top:2470px"><h4><svg class="tick" viewBox="0 0 30 30"><circle cx="15" cy="15" r="12" fill="none" stroke="#e39e2f" stroke-width="2.5"/><path d="M9 15l5 5 12-14" fill="none" stroke="#e39e2f" stroke-width="3"/></svg>Mission-Focused Approach</h4><p>Committed to safety, quality, and timely delivery, no matter the challenge.</p></div>
<div class="why-item" style="top:2581px"><h4><svg class="tick" viewBox="0 0 30 30"><circle cx="15" cy="15" r="12" fill="none" stroke="#e39e2f" stroke-width="2.5"/><path d="M9 15l5 5 12-14" fill="none" stroke="#e39e2f" stroke-width="3"/></svg>Innovative &amp; Resilient</h4><p>Leveraging modern solutions to build stronger, smarter, and more sustainable infrastructure.</p></div>
<a class="btn" style="left:114px;top:2701px;width:196px">WORK WITH US</a>

<div class="photo" style="left:610px;top:2160px;width:445px;height:288px;border:1px solid #888;background:linear-gradient(135deg,#8a8a88,#d8c48a 55%,#c9a640)" role="img" aria-label="Photo of three construction professionals in hard hats cheering"></div>
<div class="photo" style="left:658px;top:2483px;width:432px;height:279px;border:1px solid #888;background:linear-gradient(135deg,#3e4a36,#5b5b4a 45%,#8c2d2d 70%,#2f3f6a)" role="img" aria-label="Photo of military officers shaking hands in front of flags"></div>
<div class="badge" style="left:602px;top:2410px;width:142px;height:142px" aria-label="Certification badge"></div>

<!-- clients -->
<h2 class="sec-title" style="left:0;top:2906px;width:1200px;text-align:center">Trusted <span class="gold">Clients</span></h2>
<div class="client featured" style="left:114px">Harlow College</div>
<div class="client" style="left:313px">Brightfield School</div>
<div class="client" style="left:512px">Ostrand Academy</div>
<div class="client" style="left:711px">Veyport University</div>
<div class="client" style="left:910px">Calden University</div>
<a class="btn" style="left:465px;top:3230px;width:272px">VIEW OUR CREDENTIALS</a>

<!-- cta -->
<div class="photo" style="left:114px;top:3392px;width:976px;height:465px;border-radius:18px;background:linear-gradient(160deg,#3b4a5c 0%,#2a2f36 45%,#4a3524 75%,#1e1e1e 100%)" role="img" aria-label="Photo of an excavator and construction site at dusk with welding sparks"></div>
<h2 class="abs" style="left:114px;top:3530px;width:976px;text-align:center;font-size:32px;font-weight:700;line-height:45px">READY TO BUILD WITH STRENGTH<br>AND VALOR? LET’S TALK.</h2>
<a class="btn" style="left:476px;top:3652px;width:252px">REQUEST A PROPOSAL</a>

<!-- footer -->
<div class="brand" style="left:114px;top:3955px;font-size:29px"><span class="mark"></span>KESTRIM</div>
<p class="abs" style="left:114px;top:4040px;width:260px;font-size:15px;line-height:24px;color:var(--muted)">Kestrim — Building With Strength. Leading With Valor.</p>
<div class="badge" style="left:112px;top:4105px;width:74px;height:74px" aria-label="Certification badge"></div>
<div class="badge" style="left:196px;top:4105px;width:74px;height:74px" aria-label="Certification badge"></div>

<h3 class="foot-head" style="left:530px">Quick Links</h3>
<nav class="foot-links"><a>HOME</a><br><a>ABOUT US</a><br><a>SERVICES</a><br><a>PROJECTS</a><br><a>CONTACT US</a></nav>

<h3 class="foot-head" style="left:792px">Contact Info</h3>
<div class="contact-row" style="top:3977px"><span class="ico"><svg viewBox="0 0 16 16"><path d="M1 3h14v10H1z M1 3l7 6 7-6" fill="none" stroke="#fff" stroke-width="1.5"/></svg></span>info@kestrim.com</div>
<div class="contact-row" style="top:4018px"><span class="ico"><svg viewBox="0 0 16 16"><path d="M3 1l3 3-2 2c1 2 3 4 5 5l2-2 3 3-2 3C6 14 2 10 1 3z"/></svg></span>+1 (XXX) XXX-XXXX</div>
<div class="contact-row" style="top:4059px"><span class="ico"><svg viewBox="0 0 16 16"><path d="M8 1a5 5 0 0 1 5 5c0 4-5 9-5 9S3 10 3 6a5 5 0 0 1 5-5z"/><circle cx="8" cy="6" r="2" fill="#e39e2f"/></svg></span>48 ORLEN ROAD, YOUR CITY, USA</div>
<div class="abs" style="left:792px;top:4105px;display:flex;gap:10px" aria-label="Social media links">
  <span class="ico"></span><span class="ico"></span><span class="ico"></span>
</div>

<footer class="abs bottom-bar">© 2025 Kestrim. All Rights Reserved.</footer>
</body>
</html>
```